Software Engineering Company need eye catching banner for and Engineering conventions

We need an eye-catching banner designed. The size of the banner will be 34" W x 81" H. We develop routing software installed in bus systems and use GPS real-time tracking to always know where they are. We would like the banner to be dominated by the colors in our logo, 2 different blues, dark gray and of course white and black if needed. We are hoping for something that will pop out and look awesome. If you want to use our entire name or just our logo is completely up to you.

Target Market(s)

Young Engineers looking for new and cutting edge job opportunities

Industry/Entity Type

Computer Software

Colors
1f68ae
3779b6
ffffff

Requirements
Should not have
• the colors in our logo

```html
<!DOCTYPE html>
<html lang="en">
<head>
<meta charset="utf-8">
<title>Velora Technologies – Convention Banner</title>
<link rel="stylesheet" href="https://fonts.googleapis.com/css2?family=Raleway:wght@800;900&display=swap">
<style>
  :root {
    --photo-dark: #3c4650;
    --photo-warm: #8a6a48;
    --photo-light: #d9dcdc;
    --slate: #5f5f5f;
    --blue-deep: #1260b0;
    --blue-main: #2a6fb5;
    --blue-bright: #0191d9;
    --white: #ffffff;
  }
  * { margin: 0; padding: 0; box-sizing: border-box; }
  html, body { width: 1200px; height: 2860px; overflow: hidden; background: var(--white); }
  .banner {
    position: relative;
    width: 1200px;
    height: 2860px;
    overflow: hidden;
    font-family: "Raleway", "Arial Black", sans-serif;
  }
  .banner__art { position: absolute; inset: 0; display: block; }
  .brand {
    position: absolute;
    top: 70px;
    right: 34px;
    display: flex;
    align-items: center;
    gap: 22px;
    color: var(--white);
    font-weight: 800;
  }
  .brand__mark { width: 96px; height: 96px; background: var(--white); }
  .brand__text { display: flex; flex-direction: column; }
  .brand__name { font-size: 86px; line-height: 1; letter-spacing: 2px; }
  .brand__suffix { font-size: 25px; letter-spacing: 9px; margin-top: 8px; }
  .headline {
    position: absolute;
    left: 0;
    right: 0;
    top: 2005px;
    padding: 0 40px;
    text-align: center;
    color: var(--white);
    font-weight: 900;
    font-size: 102px;
    line-height: 143px;
    letter-spacing: -1px;
  }
</style>
</head>
<body>
  <main class="banner">
    <svg class="banner__art" width="1200" height="2860" viewBox="0 0 1200 2860" aria-hidden="false">
      <defs>
        <linearGradient id="photoTone" x1="0" y1="0" x2="1" y2="1">
          <stop offset="0" stop-color="var(--photo-dark)"/>
          <stop offset="0.45" stop-color="var(--photo-warm)"/>
          <stop offset="0.7" stop-color="var(--photo-light)"/>
          <stop offset="1" stop-color="var(--photo-dark)"/>
        </linearGradient>
      </defs>
      <rect class="photo-area" x="0" y="0" width="1200" height="1720" fill="url(#photoTone)"
            role="img" aria-label="Photo of a young software engineer with glasses coding at a laptop in front of a monitor"/>
      <polygon class="slate-corner" points="272,0 1200,0 1200,611" fill="var(--slate)"/>
      <polygon class="slate-arrow" points="0,749 400,994 0,1243" fill="var(--slate)"/>
      <polygon class="band-deep" points="0,1688 625,1304 894,1471 625,1641 0,2026" fill="var(--blue-deep)"/>
      <polygon class="band-bright" points="625,1641 894,1471 1200,1665 1200,1993" fill="var(--blue-bright)"/>
      <polygon class="field-main" points="0,2026 625,1641 1200,1993 1200,2860 0,2860" fill="var(--blue-main)"/>
    </svg>

    <div class="brand">
      <div class="brand__mark"></div>
      <div class="brand__text">
        <span class="brand__name">VELORA</span>
        <span class="brand__suffix">TECHNOLOGIES LLC</span>
      </div>
    </div>

    <h1 class="headline">We develop routing software installed in bus systems and use GPS real-time tracking to always know where they are</h1>
  </main>
</body>
</html>
```